Need a business card for our overland brand!

We had the logo made and we need a great design for our business card. Use the logo provide or tweak it however you see fit.

Contact Information for Business Card

Name, Title, Telephone, email, website

```html
<!DOCTYPE html>
<html lang="en">
<head>
<meta charset="utf-8">
<title>Summit Trailways – Business Card</title>
<link href="https://fonts.googleapis.com/css2?family=Arimo:wght@400;700&display=swap" rel="stylesheet">
<style>
  :root {
    --backdrop: #3d3d3d;
    --navy: #253a55;
    --teal: #1f9bc4;
    --paper: #ffffff;
    --rule: #d4d8dd;
    --ink-soft: #4a4f57;
    --mist: #eaf4f8;
  }
  * { box-sizing: border-box; margin: 0; padding: 0; }
  html, body {
    width: 1200px; height: 803px; overflow: hidden;
    background: var(--backdrop);
  }
  .stage {
    width: 1200px; height: 803px;
    display: flex; align-items: center; justify-content: center; gap: 50px;
  }
  .card {
    position: relative;
    width: 525px; height: 300px;
    border-radius: 18px;
    overflow: hidden;
  }

  /* Front side */
  .card--front { background: var(--paper); }
  .front__watermark {
    position: absolute; left: 150px; right: 30px; top: 120px; bottom: 10px;
    background: linear-gradient(160deg, rgba(234,244,248,0) 0%, var(--mist) 55%, rgba(234,244,248,0.6) 100%);
    z-index: 0;
  }
  .front__brand {
    position: absolute; top: 62px; right: 40px; z-index: 1;
    font-family: "Arimo", sans-serif; font-weight: 700;
    color: var(--navy); font-size: 30px; line-height: 1;
    white-space: nowrap;
  }
  .front__rule {
    position: absolute; left: 140px; right: 32px; top: 160px; z-index: 1;
    height: 1px; background: var(--rule);
  }
  .front__person { position: absolute; left: 40px; top: 180px; z-index: 1; }
  .person__name {
    font-family: "Arimo", sans-serif; font-weight: 700;
    color: var(--navy); font-size: 19px;
  }
  .person__title {
    font-family: "Arimo", sans-serif; font-weight: 400;
    color: var(--teal); font-size: 13px; margin-top: 2px;
  }
  .person__divider {
    width: 170px; height: 1px; background: var(--rule); margin: 8px 0 6px;
  }
  .contact { list-style: none; }
  .contact__item {
    display: flex; align-items: center; gap: 8px;
    font-family: "Arimo", sans-serif; font-size: 12px;
    color: var(--ink-soft); line-height: 16px;
  }
  .contact__icon { width: 10px; height: 10px; fill: var(--navy); flex: none; }
  .front__band {
    position: absolute; left: 0; right: 0; bottom: 0; height: 10px; z-index: 1;
    display: flex;
  }
  .band__navy { flex: 6; background: var(--navy); }
  .band__teal { flex: 4; background: var(--teal); margin-left: 3px; }

  /* Back side */
  .card--back {
    background: var(--navy);
    display: flex; align-items: center; justify-content: center;
  }
  .back__brand {
    font-family: "Arimo", sans-serif; font-weight: 700;
    color: var(--paper); font-size: 44px; line-height: 1;
    white-space: nowrap;
  }
</style>
</head>
<body>
<main class="stage">
  <section class="card card--front" aria-label="Business card front">
    <div class="front__watermark" role="img" aria-label="Faint mountain range watermark"></div>
    <div class="front__brand">Summit Trailways</div>
    <div class="front__rule"></div>
    <div class="front__person">
      <p class="person__name">Alex Morgan</p>
      <p class="person__title">President</p>
      <div class="person__divider"></div>
      <ul class="contact">
        <li class="contact__item">
          <svg class="contact__icon" viewBox="0 0 10 10"><path d="M2 0h2l1 2.5-1.3 1a6 6 0 0 0 2.8 2.8l1-1.3L10 6v2a2 2 0 0 1-2 2A8 8 0 0 1 0 2a2 2 0 0 1 2-2z"/></svg>
          555-210-4837
        </li>
        <li class="contact__item">
          <svg class="contact__icon" viewBox="0 0 10 10"><path d="M0 2h10v6H0z M0 2l5 3.5L10 2" stroke="#fff" stroke-width="0.8"/></svg>
          info@summittrailways.com
        </li>
        <li class="contact__item">
          <svg class="contact__icon" viewBox="0 0 10 10"><circle cx="5" cy="5" r="5"/><path d="M0 5h10M5 0c-2 2.5-2 7.5 0 10M5 0c2 2.5 2 7.5 0 10" stroke="#fff" stroke-width="0.7" fill="none"/></svg>
          www.summittrailways.com
        </li>
      </ul>
    </div>
    <div class="front__band"><span class="band__navy"></span><span class="band__teal"></span></div>
  </section>

  <section class="card card--back" aria-label="Business card back">
    <div class="back__brand">Summit Trailways</div>
  </section>
</main>
</body>
</html>
```